Postcard Design

I am a merchandiser for a jewelry company called marla + juniper. The jewelry style is chic with vintage inspiration. My boutique link is www.marlaandjuniper.com/boutique/dianevolkert. This is a great example to use when designing the postcard. I mainly advertise my boutique link for people to shop online for convenience. The other side is that outside of advertising my boutique link I host "pop-up shops" where a customer can host a party and earn up to $250 in free jewelry depending on how much is sold at the party. I would like my postcard to target Brides and bridemaids as I am using the postcards for a wedding fair event on January 18th. I would like to include a hook on the postcard to draw in brides/bridesmaids to be a hostess in order to earn the free jewelry credit as bridesmaids' gifts and/or bridal wear.
Updates

Payment has been guaranteed and I have added the company's logo.

Example of hostess wanted language: "Hostesses wanted! Host a pop-up in January and receive TWO retro glam pieces + $250 free jewelry credit to spend on bridesmaids' gifts and/or bridal jewelry!"

```html
<!DOCTYPE html>
<html lang="en">
<head>
<meta charset="utf-8">
<title>marla + juniper — Hostess Postcard</title>
<link rel="stylesheet" href="https://fonts.googleapis.com/css2?family=Josefin+Sans:wght@300;400&family=Cormorant+Garamond:wght@500;600&display=swap">
<style>
  :root {
    --stage: #ecebe8;
    --card: #ffffff;
    --blue: #5577ad;
    --blue-soft: #8fa6cc;
    --ink: #3b3b3b;
    --band: #d6d7da;
    --gold: #f0d96a;
    --peach: #fbe6d8;
    --peach-light: #fff7f1;
    --photo-warm: #d9b79c;
    --photo-green: #b9c48f;
  }
  * { box-sizing: border-box; margin: 0; padding: 0; }
  html, body {
    width: 1200px; height: 524px; overflow: hidden;
    background: var(--stage);
  }
  .postcard {
    position: absolute; top: 10px; height: 504px;
    background: var(--card); overflow: hidden;
    box-shadow: 0 1px 4px rgba(0,0,0,.18);
  }
  .postcard--front { left: 16px; width: 608px; }
  .postcard--back { left: 636px; width: 548px; }

  .backdrop { position: absolute; inset: 0; }

  .sunburst {
    position: absolute; left: 0; top: 0; width: 608px; height: 400px;
    background: radial-gradient(circle at 300px 120px, var(--peach-light) 0, var(--peach) 55%, #ffffff 85%);
  }

  .photo {
    position: absolute; border: 4px solid var(--gold);
    background: linear-gradient(135deg, var(--photo-warm), var(--photo-green));
  }
  .photo--one { left: 40px; top: 4px; width: 105px; height: 105px; }
  .photo--two { left: 88px; top: 116px; width: 108px; height: 110px; }
  .photo--three { left: 148px; top: 222px; width: 108px; height: 108px; }

  .offer {
    position: absolute; left: 256px; top: 40px; width: 310px;
    text-align: center; color: var(--ink);
    font-family: "Cormorant Garamond", serif; font-weight: 500;
  }
  .offer__headline {
    font-family: "Josefin Sans", sans-serif; font-weight: 300;
    color: var(--blue); font-size: 48px; line-height: 50px; letter-spacing: 1px;
  }
  .offer__rule { height: 1px; background: var(--blue-soft); margin: 6px 10px 10px; }
  .offer__line { font-size: 19px; line-height: 29px; }
  .offer__plus {
    font-family: "Josefin Sans", sans-serif; font-weight: 400;
    color: var(--blue); font-size: 36px; line-height: 34px;
  }
  .offer__credit { font-size: 18px; line-height: 21px; }

  .brand {
    position: absolute; display: flex; align-items: center; gap: 8px;
    font-family: "Josefin Sans", sans-serif; font-weight: 400; color: var(--ink);
  }
  .brand__dot { width: 14px; height: 14px; border-radius: 50%; background: var(--blue); }
  .brand--front { left: 26px; top: 432px; font-size: 24px; }
  .brand--back { left: 258px; top: 86px; font-size: 18px; }

  .contact {
    position: absolute; display: flex; align-items: center; gap: 6px;
    font-family: "Josefin Sans", sans-serif; font-weight: 400;
    color: var(--ink); font-size: 13px; white-space: nowrap;
  }
  .contact svg { width: 14px; height: 14px; flex: none; }
  .contact--front-phone { left: 236px; top: 438px; }
  .contact--front-email { left: 380px; top: 438px; }
  .contact--back-email { left: 18px; top: 352px; }
  .contact--back-phone { left: 18px; top: 372px; font-size: 15px; }
  .contact--back-link { left: 18px; top: 395px; font-size: 11px; }

  .jewel {
    position: absolute; border-radius: 50%; border: 3px solid #ffffff;
    background: radial-gradient(circle at 40% 40%, #e8d3c4, #9a7f70);
  }
  .jewel--one { left: 76px; top: 40px; width: 112px; height: 112px; }
  .jewel--two { left: 4px; top: 144px; width: 112px; height: 112px; background: radial-gradient(circle at 40% 40%, #d9c3b2, #7b5a4a); }
  .jewel--three { left: 134px; top: 158px; width: 114px; height: 114px; background: radial-gradient(circle at 40% 40%, #eadfd2, #8d7565); }
  .jewel--four { left: 70px; top: 242px; width: 108px; height: 108px; background: radial-gradient(circle at 40% 40%, #f0ead8, #b9a76f); }

  .indicia {
    position: absolute; left: 448px; top: 37px; width: 86px; height: 78px;
    border: 1.5px solid #222; padding: 6px 4px; text-align: center;
    font-family: "Josefin Sans", sans-serif; font-weight: 400; font-size: 10.5px;
    line-height: 13px; color: #111;
  }
  .address {
    position: absolute; left: 367px; top: 204px; width: 156px; height: 78px;
    border: 1.5px solid #222; padding: 16px 8px;
    font-family: "Josefin Sans", sans-serif; font-weight: 400; font-size: 13px;
    line-height: 18px; color: #111;
  }
</style>
</head>
<body>

<section class="postcard postcard--front">
  <div class="sunburst" role="img" aria-label="Soft peach sunburst backdrop"></div>
  <svg class="backdrop" width="608" height="504" viewBox="0 0 608 504">
    <path d="M380 0 H608 V30 C540 10 460 6 380 0 Z" fill="var(--blue)"/>
    <path d="M0 380 C180 350 420 356 608 372 V504 H0 Z" fill="var(--band)"/>
    <path d="M0 380 C180 350 420 356 608 372 V386 C420 372 190 368 0 398 Z" fill="var(--blue)"/>
  </svg>

  <div class="photo photo--one" role="img" aria-label="Portrait of a bride wearing floral jewellery"></div>
  <div class="photo photo--two" role="img" aria-label="Portrait of a bride with statement earrings"></div>
  <div class="photo photo--three" role="img" aria-label="Portrait of a smiling woman wearing a necklace outdoors"></div>

  <div class="offer">
    <h1 class="offer__headline">HOSTESSES<br>WANTED!</h1>
    <div class="offer__rule"></div>
    <p class="offer__line">HOST A POP-UP IN JANUARY and</p>
    <p class="offer__line">Receive TWO retro glam pieces</p>
    <p class="offer__plus">+</p>
    <p class="offer__credit">$250 free jewellery credit<br>to spend on bridesmaids' gifts<br>and/or bridal jewellery!</p>
  </div>

  <div class="brand brand--front"><span class="brand__dot"></span>marla + juniper</div>

  <div class="contact contact--front-phone">
    <svg viewBox="0 0 16 16"><circle cx="8" cy="8" r="7" fill="none" stroke="currentColor" stroke-width="1.4"/><path d="M6 4.5 L7.3 6.6 6.5 7.6 C7 8.7 7.6 9.3 8.5 9.7 L9.5 8.9 11.5 10.1 C11 11.6 9.6 11.9 8 11 6 9.8 4.6 7.8 4.7 5.6 Z" fill="currentColor"/></svg>
    (907) 555-0142
  </div>
  <div class="contact contact--front-email">
    <svg viewBox="0 0 16 16"><rect x="1" y="3" width="14" height="10" fill="currentColor"/><path d="M1.5 3.5 L8 8.5 14.5 3.5" fill="none" stroke="#fff" stroke-width="1.2"/></svg>
    dianevolkert86@postmail.net
  </div>
</section>

<section class="postcard postcard--back">
  <svg class="backdrop" width="548" height="504" viewBox="0 0 548 504">
    <path d="M0 0 H410 C340 60 320 220 250 330 C200 400 90 424 0 424 Z" fill="var(--band)"/>
    <path d="M410 0 H440 C360 70 340 230 266 340 C210 420 100 438 0 436 V424 C90 424 200 400 250 330 C320 220 340 60 410 0 Z" fill="var(--blue)"/>
  </svg>

  <div class="jewel jewel--one" role="img" aria-label="Close-up of a crystal statement necklace"></div>
  <div class="jewel jewel--two" role="img" aria-label="Layered necklaces over a plaid top"></div>
  <div class="jewel jewel--three" role="img" aria-label="Stacked gold bracelets on a wrist"></div>
  <div class="jewel jewel--four" role="img" aria-label="Jewellery displayed beside a small bird figurine"></div>

  <div class="brand brand--back"><span class="brand__dot"></span>marla + juniper</div>

  <div class="contact contact--back-email">
    <svg viewBox="0 0 16 16"><rect x="1" y="3" width="14" height="10" fill="currentColor"/><path d="M1.5 3.5 L8 8.5 14.5 3.5" fill="none" stroke="#fff" stroke-width="1.2"/></svg>
    dianevolkert86@postmail.net
  </div>
  <div class="contact contact--back-phone">
    <svg viewBox="0 0 16 16"><circle cx="8" cy="8" r="7" fill="none" stroke="currentColor" stroke-width="1.4"/><path d="M6 4.5 L7.3 6.6 6.5 7.6 C7 8.7 7.6 9.3 8.5 9.7 L9.5 8.9 11.5 10.1 C11 11.6 9.6 11.9 8 11 6 9.8 4.6 7.8 4.7 5.6 Z" fill="currentColor"/></svg>
    (907) 555-0142
  </div>
  <div class="contact contact--back-link">www.marlaandjuniper.com/boutique/dianevolkert</div>

  <div class="indicia">PRSRT STD<br>ECRWSS<br>U.S.POSTAGE<br>PAID<br>EDDM Retail</div>
  <div class="address">Local<br>Postal Customer</div>
</section>

</body>
</html>
```